Retail Consultant Business Card Design

We're looking to update the look of our very old business cards. We work primarily in the fast paced retail industry, and would like a business card that won't look dated after a few years.

We are consultants that focus primarily on shopping malls (80%), or mixed use developments (20% shopping + office space + residential). That being the case, we know that there is a lot of room for creativity. We are not a law firm, so the design doesn't have to be very static or serious. We are also not a clothing brand, so it shouldn't be too "out there" (lipstick font, jean jacket background....etc).

We're looking for something more "middle of the road", with the design leaning more towards the creative side. Our consulting firm is not very big, so we are very open to breaking away from the "traditional" or simple business card model.

One last thing that might help you, is to know who we generally hand these cards out to. It really ranges from Developers to Architects, to actual retail brands like Vela, K&T, Brentwick, Tug & Fox, Lumira...etc.

Contact Information for Business Card

Company Name: (Horizon Venture Methods Worldwide, LLC)
Individuals Name & Title
Company Address: (382 W. Alder Lane, Suite C, Tustin, CA 92781)
Telephone Number: (714) 555-0182
Fax Number: (714) 555-0147
Website: hvmworld.example
Email

Font styles to use
Serif

Colors

Designer to choose colors to be used in the design.

Requirements
Must have
• 1. The incorporation of our logo in whatever way you think would work. We have no requirements for how this should happen.
• 2. Space in the back for a QR Code, with space for instructions like
• "save us as a contact on your mobile" (or something to that effect). This will allow our clients to scan the information on the card into their phones for quick contact creation. Obviously we will handle the whole QR Code issue, but if you could mock it up , so that we could get a sense of how it would look.
• 3. Try and use brighter colors, instead of darker ones. This is really up to you, the darker colors might make other colors pop. I just mention this, because we are trying to give the sense of energy or movement, if that makes any sense.
• 4. Obviously, space for all the normal business card text (Company name, person name, phone number, email.....etc)

```html
<!DOCTYPE html>
<html lang="en">
<head>
<meta charset="utf-8">
<title>Horizon Venture Methods Worldwide – Business Card</title>
<link href="https://fonts.googleapis.com/css2?family=Tinos&family=Lato:wght@400&display=swap" rel="stylesheet">
<style>
  :root {
    --backdrop: #202022;
    --card: #161617;
    --card-edge: #2a2a2c;
    --ink: #f2f2f2;
    --ink-soft: #bdbdbd;
    --accent: #1a8ad8;
    --rule: #e6e6e6;
    --qr-field: #f2f2f2;
  }
  * { box-sizing: border-box; margin: 0; padding: 0; }
  html, body { width: 1200px; height: 900px; overflow: hidden; }
  body {
    background: var(--backdrop);
    position: relative;
    font-family: "Lato", sans-serif;
    color: var(--ink);
  }
  .card {
    position: absolute;
    left: 267px;
    width: 665px;
    height: 380px;
    background: linear-gradient(135deg, var(--card) 0%, #1d1d1f 60%, #262628 100%);
    border: 1px solid var(--card-edge);
    box-shadow: 0 10px 30px rgba(0,0,0,.45);
  }
  .card--front { top: 40px; }
  .card--back { top: 470px; }

  .brand {
    position: absolute;
    display: flex;
    align-items: center;
    gap: 26px;
  }
  .brand__dot {
    border-radius: 50%;
    background: var(--accent);
    flex: none;
  }
  .brand__name {
    font-family: "Tinos", serif;
    color: var(--ink);
    letter-spacing: .04em;
    line-height: 1.25;
  }
  .card--front .brand { left: 140px; top: 132px; }
  .card--front .brand__dot { width: 86px; height: 86px; }
  .card--front .brand__name { font-size: 23px; }

  .card--back .brand { left: 50px; top: 100px; gap: 18px; }
  .card--back .brand__dot { width: 62px; height: 62px; }
  .card--back .brand__name { font-size: 17px; }

  .qr {
    position: absolute;
    left: 50px;
    top: 196px;
    display: flex;
    align-items: center;
    gap: 16px;
  }
  .qr__field {
    width: 84px;
    height: 84px;
    background: var(--qr-field);
    border: 6px solid var(--qr-field);
    outline: 2px solid var(--accent);
    flex: none;
  }
  .qr__note {
    font-family: "Tinos", serif;
    font-size: 15px;
    line-height: 1.35;
    color: var(--ink-soft);
    letter-spacing: .02em;
  }

  .divider {
    position: absolute;
    left: 400px;
    top: 110px;
    width: 2px;
    height: 170px;
    background: var(--rule);
  }
  .contact {
    position: absolute;
    left: 428px;
    top: 96px;
  }
  .contact__name {
    font-family: "Tinos", serif;
    font-size: 29px;
    font-weight: 400;
    color: var(--accent);
    letter-spacing: .04em;
    line-height: 1;
  }
  .contact__title { font-size: 16px; margin-top: 2px; }
  .contact__address { font-size: 16px; line-height: 1.3; margin-top: 10px; }
  .contact__list { list-style: none; margin-top: 8px; }
  .contact__item {
    display: flex;
    align-items: center;
    gap: 10px;
    font-size: 17px;
    line-height: 1.45;
  }
  .contact__icon { width: 11px; height: 11px; flex: none; }
  .contact__link { color: var(--accent); }
</style>
</head>
<body>

<section class="card card--front" aria-label="Card front">
  <div class="brand">
    <span class="brand__dot"></span>
    <p class="brand__name">Horizon Venture Methods<br>Worldwide, LLC</p>
  </div>
</section>

<section class="card card--back" aria-label="Card back">
  <div class="brand">
    <span class="brand__dot"></span>
    <p class="brand__name">Horizon Venture Methods<br>Worldwide, LLC</p>
  </div>

  <div class="qr">
    <div class="qr__field" role="img" aria-label="Space for contact QR code"></div>
    <p class="qr__note">Scan to save us<br>as a contact on<br>your mobile</p>
  </div>

  <div class="divider"></div>

  <div class="contact">
    <h1 class="contact__name">Daniel Reyes</h1>
    <p class="contact__title">Director</p>
    <p class="contact__address">(382 W. Alder Lane,<br>Suite C, Tustin, CA 92781)</p>
    <ul class="contact__list">
      <li class="contact__item">
        <svg class="contact__icon" viewBox="0 0 12 12" fill="none" stroke="#1a8ad8" stroke-width="1.6"><path d="M3 1 L5 3.5 L4 5 Q5 7 7 8 L8.5 7 L11 9 L9.5 11 Q4 10 1 3 Z"/></svg>
        <span>(714) 555-0182</span>
      </li>
      <li class="contact__item">
        <svg class="contact__icon" viewBox="0 0 12 12" fill="#1a8ad8"><rect x="3" y="1" width="6" height="3"/><rect x="1" y="4.5" width="10" height="4.5" rx="1"/><rect x="3" y="8" width="6" height="3" fill="#ffffff"/></svg>
        <span>(714) 555-0147</span>
      </li>
      <li class="contact__item">
        <svg class="contact__icon" viewBox="0 0 12 12" fill="none" stroke="#1a8ad8" stroke-width="1.3"><rect x="1" y="2.5" width="10" height="7"/><path d="M1 2.5 L6 7 L11 2.5"/></svg>
        <span>info@hvmworld.example</span>
      </li>
      <li class="contact__item">
        <svg class="contact__icon" viewBox="0 0 12 12" fill="none" stroke="#1a8ad8" stroke-width="1.2"><circle cx="6" cy="6" r="5"/><ellipse cx="6" cy="6" rx="2.2" ry="5"/><path d="M1 6 H11"/></svg>
        <span>www.<span class="contact__link">hvmworld</span>.example</span>
      </li>
    </ul>
  </div>
</section>

</body>
</html>
```